Vendrick Contracting Service Flyer

We are looking to have a one page flyer designed for our services that we do
We want to keep the same colors as our logo

Requirements
Must have
• Our Name should be in Onyx Font
• Colors Used:
• 070bac
• b3b4e6
• fbd234

```html
<!DOCTYPE html>
<html lang="en">
<head>
<meta charset="utf-8">
<title>Vendrick Contracting – Our Services</title>
<link href="https://fonts.googleapis.com/css2?family=Bodoni+Moda:opsz,wght@6..96,500;6..96,700&family=Bebas+Neue&family=Roboto:wght@400&display=swap" rel="stylesheet">
<style>
  :root {
    --backdrop: #3b3b3d;
    --paper: #ffffff;
    --blue: #2b3893;
    --lilac: #b3b4dd;
    --yellow: #f8d435;
    --ink: #3a3a3a;
  }
  * { margin: 0; padding: 0; box-sizing: border-box; }
  html, body { width: 871px; height: 1200px; overflow: hidden; background: var(--backdrop); }
  .canvas { position: relative; width: 871px; height: 1200px; }
  .flyer { position: absolute; left: 54px; top: 60px; width: 763px; height: 1079px; background: var(--paper); overflow: hidden; }
  .band-top { position: absolute; left: 0; top: 0; width: 100%; height: 34px; background: var(--blue); }
  .band-yellow { position: absolute; left: 0; top: 34px; width: 100%; height: 66px; background: var(--yellow); }
  .shapes { position: absolute; left: 0; top: 0; }
  .title {
    position: absolute; left: 386px; top: 60px;
    font-family: "Bodoni Moda", serif; font-weight: 700; font-size: 86px; line-height: 1;
    color: var(--blue); white-space: nowrap;
    transform: translateX(-50%) scaleX(0.47); transform-origin: center top;
  }
  .service-list {
    position: absolute; top: 180px; list-style: none;
    font-family: "Bodoni Moda", serif; font-weight: 700; font-size: 32px; line-height: 33.9px;
    color: var(--blue); white-space: nowrap;
    transform: scaleX(0.5); transform-origin: left top;
  }
  .service-list.left { left: 65px; }
  .service-list.right { left: 406px; }
  .brand { position: absolute; left: 402px; top: 561px; color: var(--blue); font-family: "Bodoni Moda", serif; font-weight: 700; white-space: nowrap; }
  .brand-name { display: block; font-size: 88px; line-height: 1; letter-spacing: 2px; transform: scaleX(0.45); transform-origin: left top; }
  .brand-sub { display: block; margin-top: -4px; padding-left: 4px; font-size: 28px; line-height: 1.1; letter-spacing: 7px; }
  .perks { position: absolute; left: 65px; top: 813px; list-style: none; font-family: "Bebas Neue", sans-serif; font-size: 24px; line-height: 43.4px; color: var(--ink); letter-spacing: 2.3px; white-space: nowrap; }
  .contact { position: absolute; left: 64px; top: 1029px; display: flex; align-items: center; font-family: "Roboto", sans-serif; font-size: 15.5px; color: var(--blue); letter-spacing: 0.4px; white-space: nowrap; }
  .contact-item { display: flex; align-items: center; gap: 8px; }
  .contact-item.web { margin-right: 20px; }
  .contact-item.phone { margin-right: 28px; }
  .contact-item svg { width: 20px; height: 20px; fill: var(--blue); }
</style>
</head>
<body>
<div class="canvas">
  <div class="flyer">
    <div class="band-top"></div>
    <div class="band-yellow"></div>

    <svg class="shapes" width="763" height="1079" viewBox="0 0 763 1079" aria-hidden="true">
      <polygon points="244,665 300,650 763,862 763,904" fill="var(--lilac)"/>
      <polygon points="0,552 763,904 763,952 0,604" fill="var(--blue)"/>
      <polygon points="0,604 763,952 763,1079 0,1079" fill="var(--yellow)"/>
    </svg>

    <h1 class="title">OUR SERVICES</h1>

    <ul class="service-list left">
      <li>Exterior &amp; Interior Painting</li>
      <li>General Carpentry</li>
      <li>Framing Repairs</li>
      <li>Siding/Gutters/Windows/Doors</li>
      <li>Concrete Walkways/Stoops</li>
      <li>Balcony/Deck Rehab</li>
      <li>Tuckpointing</li>
      <li>Sealants/Caulks</li>
      <li>Pressure Washing</li>
      <li>Specialty Coatings</li>
    </ul>

    <ul class="service-list right">
      <li>Drywall Install/Repair</li>
      <li>Plaster Repairs</li>
      <li>Wallpaper Removal</li>
      <li>Flooring/Tile/Carpet/Hardwood/Vinyl</li>
      <li>Leak Investigations:</li>
      <li>-Facades, Roofs, Interior Leaks</li>
      <li>EIFS/Stucco Repairs</li>
      <li>Plumbing Repairs</li>
      <li>Roofing Repairs</li>
      <li>Lead Safe Renovations</li>
    </ul>

    <div class="brand">
      <span class="brand-name">VENDRICK</span>
      <span class="brand-sub">Contracting</span>
    </div>

    <ul class="perks">
      <li>Quick Estimates</li>
      <li>Yearly Maintenance Contracts</li>
      <li>Fast Repsonse to General Service Work Order Repairs,</li>
      <li>Guaranteed!!!</li>
    </ul>

    <div class="contact">
      <span class="contact-item web">
        <svg viewBox="0 0 24 24" aria-hidden="true"><path d="M12 2a10 10 0 1 0 0 20 10 10 0 0 0 0-20zm6.9 6h-2.9a15.7 15.7 0 0 0-1.4-3.6A8 8 0 0 1 18.9 8zM12 4c.8 1.2 1.5 2.5 1.9 4h-3.8c.4-1.5 1.1-2.8 1.9-4zM4.3 14a8.2 8.2 0 0 1 0-4h3.4a16.5 16.5 0 0 0 0 4H4.3zm.8 2h2.9c.3 1.3.8 2.5 1.4 3.6A8 8 0 0 1 5.1 16zM8 8H5.1a8 8 0 0 1 4.3-3.6C8.8 5.5 8.4 6.7 8 8zm4 12c-.8-1.2-1.5-2.5-1.9-4h3.8c-.4 1.5-1.1 2.8-1.9 4zm2.3-6H9.7a14.7 14.7 0 0 1 0-4h4.6a14.7 14.7 0 0 1 0 4zm.3 5.6c.6-1.1 1.1-2.3 1.4-3.6h2.9a8 8 0 0 1-4.3 3.6zm1.7-5.6a16.5 16.5 0 0 0 0-4h3.4a8.2 8.2 0 0 1 0 4h-3.4z"/></svg>
        vendrickcontracting.com
      </span>
      <span class="contact-item phone">
        <svg viewBox="0 0 24 24" aria-hidden="true"><path d="M6.6 10.8a15.1 15.1 0 0 0 6.6 6.6l2.2-2.2c.3-.3.7-.4 1-.2 1.1.4 2.3.6 3.6.6.6 0 1 .4 1 1V20c0 .6-.4 1-1 1A17 17 0 0 1 3 4c0-.6.4-1 1-1h3.5c.6 0 1 .4 1 1 0 1.3.2 2.5.6 3.6.1.3 0 .7-.2 1l-2.3 2.2z"/></svg>
        555.014.0287
      </span>
      <span class="contact-item mail">
        <svg viewBox="0 0 24 24" aria-hidden="true"><path d="M2 5h20v14H2V5zm2 2v.4l8 5.3 8-5.3V7H4zm16 2.8-8 5.3-8-5.3V17h16V9.8z"/></svg>
        info@vendrickcontracting.com
      </span>
    </div>
  </div>
</div>
</body>
</html>
```